Website for the new investment company.

We are building a website for a new company. This will be an investment company. The name of the company is Tern Harbor Equity, or THE. We don't have a company logo yet, so happy to take suggestions on that as well (and will add that to the final cost). The investors of this company will exclusively be Dunmore College alumni graduates. The investors are not students, but instead older professionals in various industries, that previously graduated from the Dunmore College. This company will establish an investment fund and invest in multiple businesses.
The purpose of the website will be to educate Dunmore alumni on the investment fund.
We are looking for:
1. The design to be relatable, but not the copy of the Dunmore College website. https://www.dunmorecol.edu/
2. This is an investment website and must mimic other similar websites
https://plovergate-fund.com/
https://www.brindlevest.com/
https://kestowholdings.com/site/global/home/p_home.gsp
3. Project timeline. We are focused on receiving a design in the next two weeks and then finishing the website over the following 2 weeks. We anticipate paying for additional work and customization after the designs are provided.
4. Website Pages:
1) Homepage - Mission and Objective (high quality photos along with text that we will provide after selecting the winning design)
2) Background - Text and biographies on the 2 founders (high quality photos along with text that we will provide after selecting the winning design)
3) Advisory Board - Text and biographies on the investment Fund's 3 advisory board members (high quality photos along with text that we will provide after selecting the winning design)
4) Fund I - Text and information on the specific investment fund including pictures and biographies of the investment committee (high quality photos along with text that we will provide after selecting the winning design)
5) Contact Us - Typical website contact page for visitors

Target Market(s)

Dunmore Alumni graduates

Industry/Entity Type

Investment

Coding

Coded - Design and coding required

Font styles to use
Serif
Sans Serif

Colors
0054AA
0677BA
7BADD7
CADEEF
E8F1F8

Requirements
Must have
• Must look like other private investment websites as provided in project description
Nice to have
• Mimics the Dunmore College style, but definitely needs to be different. This company has no direct relationship with Dunmore College.
Should not have
• No commercial transactions, no credit card payments etc. Do not replicate any logos, designs or proprietary content from Dunmore College.

```html
<!DOCTYPE html>
<html lang="en">
<head>
<meta charset="utf-8">
<title>Tern Harbor Equity</title>
<link rel="stylesheet" href="https://fonts.googleapis.com/css2?family=EB+Garamond:ital,wght@0,500;0,600;0,700;1,500;1,600&family=Lato:wght@400;700&display=swap">
<style>
  :root {
    --brand-blue: #0054AA;
    --mid-blue: #0677BA;
    --soft-blue: #7BADD7;
    --pale-blue: #CADEEF;
    --mist: #E8F1F8;
    --navy: #12124a;
    --footer: #13133f;
    --ink: #222;
    --white: #fff;
  }
  * { margin: 0; padding: 0; box-sizing: border-box; }
  html, body { width: 861px; height: 1200px; overflow: hidden; background: var(--white); }
  body { position: relative; font-family: 'Lato', sans-serif; color: var(--ink); }

  .site-header { position: absolute; top: 0; left: 0; width: 861px; height: 75px; background: var(--white); }
  .brand-name { position: absolute; font-family: 'EB Garamond', serif; font-weight: 600; font-size: 21px; line-height: 24px; white-space: nowrap; }
  .site-header .brand-name { left: 80px; top: 26px; color: var(--brand-blue); }
  .main-nav { position: absolute; left: 398px; top: 31px; display: flex; gap: 17px; font-size: 10.8px; }
  .main-nav a { color: #333; text-decoration: none; }
  .main-nav a.is-active { color: var(--brand-blue); }
  .btn { display: flex; align-items: center; justify-content: center; background: linear-gradient(90deg, #0b2f78, var(--navy)); color: var(--white); font-weight: 700; font-size: 11px; border-radius: 2px; text-decoration: none; position: absolute; }
  .btn-start { left: 664px; top: 22px; width: 118px; height: 33px; }

  .hero { position: absolute; top: 75px; left: 0; width: 861px; height: 338px; background: var(--brand-blue); overflow: hidden; }
  .hero-photo { position: absolute; inset: 0; background: linear-gradient(180deg, #a9b4c6 0%, #6f8db8 30%, #3e6ead 58%, var(--brand-blue) 80%); }
  .hero-title { position: absolute; top: 196px; width: 100%; text-align: center; font-family: 'EB Garamond', serif; font-weight: 700; font-size: 23px; color: var(--white); letter-spacing: 0.2px; }
  .hero-sub { position: absolute; top: 233px; left: 180px; width: 501px; text-align: center; font-family: 'EB Garamond', serif; font-weight: 700; font-size: 19px; line-height: 25.5px; color: var(--white); }
  .slider-dots span { position: absolute; top: 305px; height: 2.5px; width: 27px; background: var(--soft-blue); border-radius: 2px; }
  .slider-dots span.is-current { background: var(--white); }

  .about-title { position: absolute; left: 82px; top: 468px; font-family: 'EB Garamond', serif; font-weight: 700; font-size: 30px; color: var(--brand-blue); letter-spacing: 0.3px; }
  .about-title span { color: var(--navy); }
  .about-lead { position: absolute; left: 81px; top: 526px; font-size: 11.7px; color: #222; }
  .about-copy { position: absolute; left: 82px; width: 328px; font-size: 10.5px; line-height: 19.7px; color: #333; }
  .btn-learn { left: 82px; top: 720px; width: 109px; height: 33px; }
  .about-frame { position: absolute; left: 462px; top: 484px; width: 295px; height: 277px; background: #a3bad8; }
  .about-photo { position: absolute; left: 478px; top: 470px; width: 303px; height: 277px; background: linear-gradient(135deg, #3a5c78 0%, #22324a 55%, #141c2c 100%); }

  .testimonial { position: absolute; top: 813px; left: 0; width: 861px; height: 285px; background: linear-gradient(180deg, #0050a8, var(--brand-blue)); }
  .quote-mark { position: absolute; }
  .quote-text { position: absolute; top: 76px; width: 100%; text-align: center; font-family: 'EB Garamond', serif; font-style: italic; font-weight: 600; font-size: 29.5px; line-height: 36px; color: var(--white); }
  .quote-author { position: absolute; top: 198px; width: 100%; text-align: center; font-size: 14.5px; color: var(--white); }

  .site-footer { position: absolute; top: 1098px; left: 0; width: 861px; height: 102px; background: var(--footer); }
  .site-footer .brand-name { left: 80px; top: 39px; color: var(--white); }
  .copyright { position: absolute; right: 79px; top: 45px; font-size: 11px; color: var(--white); }
</style>
</head>
<body>
  <header class="site-header">
    <div class="brand-name">Tern Harbor Equity</div>
    <nav class="main-nav">
      <a class="is-active" href="#">Home</a>
      <a href="#">About Us</a>
      <a href="#">Contact Us</a>
      <a href="#">Investments</a>
    </nav>
    <a class="btn btn-start" href="#">GET STARTED</a>
  </header>

  <section class="hero">
    <div class="hero-photo" role="img" aria-label="Photo of a hand over stacks of coins with a rising growth chart for 2019 to 2022"></div>
    <h1 class="hero-title">UNLOCKING FINANCIAL INSIGHTS</h1>
    <p class="hero-sub">EMPOWERING DUNMORE ALUMNI WITH INVESTMENT KNOWLEDGE</p>
    <div class="slider-dots">
      <span class="is-current" style="left:380px"></span>
      <span style="left:418px"></span>
      <span style="left:454px"></span>
    </div>
  </section>

  <section class="about">
    <h2 class="about-title">ABOUT <span>US</span></h2>
    <p class="about-lead">Risus commodo viverra maecenas ac cumsan lacu.</p>
    <p class="about-copy" style="top:550px">Lorem ipsum dolor sit amet, consectetur adipiscing elit, sed do eius mod tempor incididunt ut labore et dolore magna aliqua. Quis ipsum suspendisse ultrices gravida. Risus commodo viverra maecenas ac cumsan lacus vel facilisis.</p>
    <p class="about-copy" style="top:636px">Lorem ipsum dolor sit amet, consectetur adipiscing elit, sed do eius mod tempor incididunt ut labore et dolore magna aliqua. Quis ipsum suspendisse ultrices gravida.</p>
    <a class="btn btn-learn" href="#">LEARN MORE</a>
    <div class="about-frame"></div>
    <div class="about-photo" role="img" aria-label="Photo of three colleagues reviewing documents at a desk in an office at night"></div>
  </section>

  <section class="testimonial">
    <svg class="quote-mark" style="left:80px;top:40px" width="68" height="48" viewBox="0 0 68 48" fill="none" stroke="#7BADD7" stroke-width="1.6">
      <path d="M14 46 C6 38 1 30 1 18 C1 8 7 1 15 1 C23 1 29 7 29 15 C29 23 23 28 16 28 C16 34 18 40 22 44 Z"/>
      <path d="M52 46 C44 38 39 30 39 18 C39 8 45 1 53 1 C61 1 67 7 67 15 C67 23 61 28 54 28 C54 34 56 40 60 44 Z"/>
    </svg>
    <p class="quote-text">Quis ipsum suspendisse ultrices gravi da.<br>Risus commodo viverra maecenas actkt<br>cumsan lacus vel facilisis.</p>
    <p class="quote-author">Marlo Venning</p>
    <svg class="quote-mark" style="left:713px;top:178px" width="68" height="48" viewBox="0 0 68 48" fill="none" stroke="#7BADD7" stroke-width="1.6">
      <path d="M15 2 C23 10 28 18 28 30 C28 40 22 47 14 47 C6 47 1 41 1 33 C1 25 7 20 14 20 C14 14 12 8 8 4 Z"/>
      <path d="M53 2 C61 10 66 18 66 30 C66 40 60 47 52 47 C44 47 39 41 39 33 C39 25 45 20 52 20 C52 14 50 8 46 4 Z"/>
    </svg>
  </section>

  <footer class="site-footer">
    <div class="brand-name">Tern Harbor Equity</div>
    <p class="copyright">2024 Tern Harbor Equity. All Rights Reserved.</p>
  </footer>
</body>
</html>
```